Sell the dream! Property investment proposal document

We are looking for a proposal document which outlines our vision for property development. The purpose of the document is to raise investment from investors - sell the dream!
Brief summary:
Tarrow Dwellings Developments, is an emerging New Zealand property investment company with a focus on providing unique property investment opportunities.
Our expertise and capabilities in architectural modular homes provide us with a remarkable advantage in tackling the development of properties that are typically considered challenging, remote, or uniquely positioned.
Our specialization in this niche sector of property development not only sets us apart from competitors, but also paves the way for lucrative investment opportunities in the New Zealand property market.
Feel free to use any images from www.tarrowdwellings.co.nz
Target Market(s)
investors for a unique property development opportunity
Industry/Entity Type
luxury property development in unique locations throughout New Zealand
Font styles to use
Colors
Designer to choose only greyscale colors for use in the design.
Look and feel

```html
<!DOCTYPE html>
<html lang="en">
<head>
<meta charset="utf-8">
<title>Tarrow Dwellings Developments – Investment Proposal</title>
<link href="https://fonts.googleapis.com/css2?family=Noto+Sans:wght@500&family=Source+Sans+3:wght@300;400&display=swap" rel="stylesheet">
<style>
  :root {
    --page-bg: #ececec;
    --panel: #323232;
    --panel-edge: #2a2a2a;
    --ink: #f3f3f3;
    --ink-soft: #d6d6d6;
    --photo-ground: #4e5a3a;
    --photo-dusk: #6b5a3c;
    --photo-dark: #2b2b2b;
    --accent-bar: #8a6a1e;
  }
  * { box-sizing: border-box; margin: 0; padding: 0; }
  html, body {
    width: 1200px; height: 753px; overflow: hidden;
    background: var(--page-bg);
    font-family: "Source Sans 3", sans-serif;
    color: var(--ink);
  }
  .brochure {
    position: absolute; left: 30px; top: 46px;
    width: 1140px; height: 660px;
    display: flex;
    box-shadow: 0 10px 30px rgba(0,0,0,.25);
  }
  .panel {
    position: relative; width: 380px; height: 660px;
    background: var(--panel);
    border-right: 1px solid var(--panel-edge);
    overflow: hidden;
  }
  .panel:last-child { border-right: none; }
  .photo { position: absolute; }
  .heading {
    position: absolute;
    font-family: "Noto Sans", sans-serif; font-weight: 500;
    color: var(--ink); letter-spacing: .2px; white-space: nowrap; line-height: 1.2;
  }
  .copy { position: absolute; color: var(--ink-soft); font-weight: 400; }
  .copy p { margin-bottom: 9px; }
  .wordmark {
    position: absolute;
    font-family: "Source Sans 3", sans-serif; font-weight: 300;
    color: var(--ink); line-height: 1;
  }

  /* Panel 1 */
  .accent-frame { position: absolute; left: 6px; top: 64px; width: 150px; height: 210px; background: var(--accent-bar); }
  .p1-hero { left: 12px; top: 58px; width: 150px; height: 210px; background: linear-gradient(180deg, #e4e9ee 0%, #c9d1d8 50%, var(--photo-ground) 85%); }
  .p1-title { left: 170px; top: 36px; font-size: 17px; }
  .p1-copy { left: 170px; top: 68px; width: 198px; font-size: 8.4px; line-height: 1.55; }
  .p1-interior { left: 8px; top: 285px; width: 182px; height: 120px; background: linear-gradient(180deg, #b7c3cf 0%, #7e8d78 55%, #5b6a44 100%); }
  .p1-landscape { left: 196px; top: 283px; width: 176px; height: 122px; background: linear-gradient(180deg, #8a8468 0%, var(--photo-dusk) 50%, #3c3a26 100%); }
  .p1-summary-title { left: 0; width: 100%; top: 420px; text-align: center; font-size: 17px; }
  .p1-summary { left: 14px; top: 454px; width: 352px; text-align: center; font-size: 7.2px; line-height: 1.55; }
  .p1-summary p { margin-bottom: 8px; }

  /* Panel 2 */
  .p2-hero { left: 18px; top: 100px; width: 344px; height: 280px; background: linear-gradient(180deg, #a9b5c4 0%, #8e9aa6 45%, #3c3c3c 62%, #56683c 80%, #4a5a32 100%); }
  .p2-wordmark { left: 26px; top: 12px; font-size: 104px; letter-spacing: -2px; }
  .p2-title { left: 18px; top: 400px; font-size: 20px; }
  .bullets { position: absolute; list-style: none; font-size: 5.8px; line-height: 1.7; color: var(--ink-soft); }
  .bullets li { position: relative; padding-left: 10px; margin-bottom: 9px; }
  .bullets li::before {
    content: ""; position: absolute; left: 0; top: 2px;
    width: 4px; height: 4px; border: 1px solid var(--ink); border-radius: 50%;
  }
  .p2-bullets-a { left: 18px; top: 438px; width: 215px; }
  .p2-view { left: 246px; top: 402px; width: 116px; height: 124px; background: linear-gradient(180deg, #c6d4e2 0%, #5d7f9e 50%, #2e3e4e 70%, var(--photo-dark) 100%); }
  .p2-villa { left: 18px; top: 545px; width: 178px; height: 100px; background: linear-gradient(180deg, #9fb4c8 0%, #7d8c8c 55%, #4d5a3a 100%); }
  .p2-bullets-b { left: 202px; top: 544px; width: 172px; font-size: 5.2px; line-height: 1.5; }
  .p2-bullets-b li { margin-bottom: 6px; }

  /* Panel 3 */
  .p3-wordmark { right: 16px; top: 16px; font-size: 58px; letter-spacing: -1px; }
  .p3-title { right: 16px; top: 80px; font-size: 18px; }
  .p3-cliff { left: 10px; top: 108px; width: 162px; height: 200px; background: linear-gradient(180deg, #c7b690 0%, #8e8a80 40%, #6e6252 75%, #4f4234 100%); }
  .p3-house { left: 172px; top: 132px; width: 208px; height: 200px; background: linear-gradient(180deg, #c3c7cc 0%, #8b8e92 35%, #2e2e2e 60%, #56624a 100%); }
  .p3-garden { left: 52px; top: 308px; width: 120px; height: 24px; background: linear-gradient(180deg, #55624a 0%, #3e4a34 100%); }
  .p3-copy { left: 14px; top: 358px; width: 352px; text-align: center; font-size: 7.2px; line-height: 1.75; }
  .p3-copy p { margin-bottom: 14px; }
</style>
</head>
<body>
<main class="brochure">

  <section class="panel panel--advantage">
    <div class="accent-frame"></div>
    <div class="photo p1-hero" role="img" aria-label="Photo of a dark cantilevered modular home on a grassy coastal hillside"></div>
    <h2 class="heading p1-title">Competitive Advantage</h2>
    <div class="copy p1-copy">
      <p>Our competitive advantage lies in the uniqueness of our property investment opportunities. Unlike traditional real estate companies, we focus on offering properties that are not only profitable but also aesthetically pleasing and unique. By catering to the tastes of architecture lovers, we set ourselves apart from the competition and attract a niche market of customers who appreciate the artistry and design of our projects.</p>
      <p>Additionally, the streamlined and condensed timelines facilitated by our modular approach provide quicker returns on investment.</p>
    </div>
    <div class="photo p1-interior" role="img" aria-label="Photo of a bright interior with floor-to-ceiling glass overlooking a bay and hills"></div>
    <div class="photo p1-landscape" role="img" aria-label="Photo of a low modular home in golden rural farmland at dusk"></div>
    <h2 class="heading p1-summary-title">Financial Summary</h2>
    <div class="copy p1-summary">
      <p>In terms of financial projections, with each development, we anticipate a profit of 10%-20% which will be project dependent.</p>
      <p>This growth is fueled by the increasing demand for unique property investments in New Zealand and our ability to deliver high-quality services to the market in a condensed time frame, with heavily controlled costs.</p>
      <p>With a solid business model and a dedicated team, we are confident in our ability to achieve success and establish Tarrow Dwellings Investments as a trusted name in the industry.</p>
      <p>New Zealand's property market has been experiencing steady growth over the years, making it an attractive destination for property investors. With its beautiful landscapes and strong economy, New Zealand offers a diverse range of investment opportunities for both local and international investors. The demand for quality properties in prime locations continues to rise, creating a favorable environment for property investment companies like ours that can lean on our modular benefits of being able to reach unique and remote locations</p>
    </div>
  </section>

  <section class="panel panel--overview">
    <div class="photo p2-hero" role="img" aria-label="Photo of a dark modern home with lit terrace, lawn and trees at dusk"></div>
    <div class="wordmark p2-wordmark">Tarrow</div>
    <h2 class="heading p2-title">Business Overview</h2>
    <ul class="bullets p2-bullets-a">
      <li>Tarrow Dwellings Developments, is an emerging New Zealand property investment company with a focus on providing unique property investment opportunities.</li>
      <li>Our expertise and capabilities in architectural modular homes provide us with a remarkable advantage in tackling the development of properties that are typically considered challenging, remote, or uniquely positioned.</li>
      <li>As a company, with 48 employees boasting a wealth of experience in handling complex architectural projects, making us well-equipped to navigate the intricacies and demands of such ventures.</li>
    </ul>
    <div class="photo p2-view" role="img" aria-label="Photo of a lounge chair facing a wide ocean view through large windows"></div>
    <div class="photo p2-villa" role="img" aria-label="Photo of a long modular home among native bush and a tall tree"></div>
    <ul class="bullets p2-bullets-b">
      <li>This advantage allows us to not only execute projects efficiently but also to deliver exceptional results within condensed time frames.</li>
      <li>By capitalizing on our ability to develop difficult, remote, or one-of-a-kind properties swiftly and effectively, Tarrow Dwellings Developments offers investors a rare chance to engage in projects that promise exceptional profitability in the New Zealand property market.</li>
      <li>Our specialization in this niche sector of property development not only sets us apart from competitors, but also paves the way for lucrative investment opportunities in the New Zealand property market.</li>
    </ul>
  </section>

  <section class="panel panel--origins">
    <div class="wordmark p3-wordmark">Tarrow</div>
    <h2 class="heading p3-title">Business Origins</h2>
    <div class="photo p3-cliff" role="img" aria-label="Photo of a glass pavilion on a gravel clifftop overlooking the sea at sunset"></div>
    <div class="photo p3-house" role="img" aria-label="Photo of a dark timber-clad home with garage and planted driveway"></div>
    <div class="photo p3-garden" role="img" aria-label="Photo detail of native garden planting"></div>
    <div class="copy p3-copy">
      <p>Tarrow Dwellings Developments was established with the goal of transforming the property investment market in New Zealand by introducing an innovative approach that centers on architectural modular designs and streamlined project timelines.</p>
      <p>Driven by our enthusiasm for architecture and real estate, we have expanded our successful business model to not only offer financial opportunities for investors but also to expand on our passion for high-end architectural design</p>
      <p>With a wealth of experience accumulated over the past six years in the construction and the property market, we are pivoting to focus solely on our property development initiatives, presenting completed Tarrow projects to the market, in exclusive locations.</p>
      <p>These projects will boast high-quality standards, meticulous attention to detail and landscaping, and creative design elements. By introducing completed Tarrow properties into the market, we aim to reach a wider audience, catering to individuals who prefer ready-to-occupy homes, over engaging in the design and construction process. This approach also simplifies the financing process for prospective buyers, as established properties are often preferred by financial lenders</p>
    </div>
  </section>

</main>
</body>
</html>
```